Land Buying Company Needs Letterhead for Direct Mail Marketing to Land Owners

We are looking for a professional letterhead that we will be including in our direct mail marketing. We will be sending this to land owners who may be interested in selling or purchasing land.

The letterhead needs to be editable. Headers and footers would look nice, but we are open. We would want it to include our address, website, phone, and email info. For right now the address to use for design purposes would the following:

Address: 415 Bramwell Avenue #600
Dallas, TX 75219
Website - www.quillridgeacres.example
Email - info@quillridgeacres.example
Phone - 866-402-ACRE

I have attached our logo zip file that we just had done on Pixel Guild. Let me know what questions you have, and thank you.

```html
<!DOCTYPE html>
<html lang="en">
<head>
<meta charset="utf-8">
<title>Quillridge Acres Letterhead</title>
<link href="https://fonts.googleapis.com/css2?family=Lato:wght@400;700&family=Montserrat:wght@700&family=Satisfy&display=swap" rel="stylesheet">
<style>
  :root {
    --backdrop: #dedede;
    --paper-top: #f4f2f3;
    --paper-bottom: #e3e3e4;
    --ink: #2f2f31;
    --brand-dark: #3f5f1c;
    --brand-lime: #8cc63f;
  }
  * { margin: 0; padding: 0; box-sizing: border-box; }
  html, body { width: 1200px; height: 1145px; overflow: hidden; }
  body { background: var(--backdrop); font-family: "Lato", sans-serif; color: var(--ink); }

  .letterhead {
    position: absolute; left: 171px; top: 20px;
    width: 858px; height: 1105px;
    background: linear-gradient(180deg, var(--paper-top) 0%, var(--paper-top) 30%, var(--paper-bottom) 100%);
  }

  .brand { position: absolute; display: flex; align-items: center; }
  .brand-mark { border-radius: 50%; background: var(--brand-dark); flex: none; }
  .brand-name {
    font-family: "Montserrat", sans-serif; font-weight: 700;
    color: var(--brand-dark); text-transform: uppercase; line-height: 1.05;
  }
  .brand--header { left: 77px; top: 54px; gap: 14px; }
  .brand--header .brand-mark { width: 64px; height: 64px; }
  .brand--header .brand-name { font-size: 30px; }
  .brand--footer { left: 602px; top: 1030px; gap: 12px; }
  .brand--footer .brand-mark { width: 50px; height: 50px; }
  .brand--footer .brand-name { font-size: 21px; }

  .contact-list {
    position: absolute; right: 12px; top: 32px; list-style: none;
    font-size: 17.5px; line-height: 25px;
  }
  .contact-list li { display: flex; align-items: center; gap: 7px; }
  .contact-list svg { width: 17px; height: 17px; flex: none; }

  .letter { position: absolute; left: 75px; top: 252px; width: 699px; font-size: 16px; line-height: 19px; }
  .letter-date { margin-bottom: 22px; font-size: 17px; }
  .recipient { margin-bottom: 21px; font-size: 16px; }
  .salutation { font-size: 20px; font-weight: 700; margin-bottom: 18px; }
  .letter-body p { text-align: justify; margin-bottom: 18px; }
  .closing { margin-top: 30px; }
  .signature { font-family: "Satisfy", cursive; font-size: 38px; margin-top: 22px; color: #222; }

  .footer-address { position: absolute; left: 77px; top: 1036px; font-size: 21px; }
  .footer-rule { position: absolute; left: 0; top: 1068px; width: 604px; height: 3px; background: var(--brand-dark); }
</style>
</head>
<body>
<main class="letterhead">
  <header>
    <div class="brand brand--header">
      <span class="brand-mark"></span>
      <span class="brand-name">Quillridge<br>Acres</span>
    </div>
    <ul class="contact-list">
      <li>
        <svg viewBox="0 0 24 24" fill="none" stroke="#3f5f1c" stroke-width="2"><circle cx="12" cy="12" r="10"/><path d="M8 7l2 0 1 3-1.5 1a7 7 0 0 0 3.5 3.5l1-1.5 3 1v2c0 1-1 2-2 2A11 11 0 0 1 6 9c0-1 1-2 2-2z"/></svg>
        866-402-ACRE
      </li>
      <li>
        <svg viewBox="0 0 24 24" fill="none" stroke="#3f5f1c" stroke-width="1.6"><rect x="2" y="5" width="20" height="14"/><path d="M2 5l10 8 10-8"/></svg>
        info@quillridgeacres.example
      </li>
      <li>
        <svg viewBox="0 0 24 24" fill="none" stroke="#3f5f1c" stroke-width="1.8"><circle cx="12" cy="12" r="10"/><path d="M2 12h20M12 2c3 3 3 17 0 20M12 2c-3 3-3 17 0 20"/></svg>
        www.quillridgeacres.example
      </li>
    </ul>
  </header>

  <article class="letter">
    <p class="letter-date">June -22-2020</p>
    <p class="recipient">Mr, Peter Vance<br>President</p>
    <p class="recipient">Fenwick Holdings<br>123 Street Name, Suite# 10<br>City, State, 120023</p>
    <p class="salutation">Dear Mr, Peter</p>
    <div class="letter-body">
      <p>Lorem ipsum dolor sit amet, consectetur adipisicing elit, sed do eiusmod tempor incididunt ut labore et dolore magna aliqua. Ut enim ad minim veniam, quis nostrud exercitation ullamco laboris nisi ut aliquip ex ea commodo consequat. Duis aute irure dolor in reprehenderit in voluptate velit esse cillum dolore eu fugiat nulla pariatur.</p>
      <p>Lorem ipsum dolor sit amet, consectetur adipisicing elit, sed do eiusmod tempor incididunt ut labore et dolore magna aliqua. Ut enim ad minim veniam, quis nostrud exercitation ullamco laboris nisi ut aliquip ex ea commodo consequat. Duis aute irure dolor in reprehenderit in voluptate velit esse cillum dolore eu fugiat nulla pariatur.</p>
      <p>Lorem ipsum dolor sit amet, consectetur adipisicing elit, sed do eiusmod tempor incididunt ut labore et dolore magna aliqua. Ut enim ad minim veniam, quis nostrud exercitation ullamco laboris nisi ut aliquip ex ea commodo consequat.</p>
      <p>Excepteur sint occaecat cupidatat non proident, sunt in culpa qui officia deserunt mollit anim id est laborum. re et dolore magnam aliquam quaerat voluptatem.</p>
    </div>
    <p class="closing">Regards</p>
    <p class="signature">Daniel Harlow</p>
  </article>

  <footer>
    <p class="footer-address">415 Bramwell Avenue #600 Dallas, TX 75219</p>
    <div class="footer-rule"></div>
    <div class="brand brand--footer">
      <span class="brand-mark"></span>
      <span class="brand-name">Quillridge<br>Acres</span>
    </div>
  </footer>
</main>
</body>
</html>
```